Business Card Design Project

We are rebranding an existing automotive collision repair business. The business is called dentworks garage. I have attached logo but I'm not tied to that. I want to leave this wide open.

I want this card to say we are professional, competent, cutting edge. We are focused on customers and use a lot of the latest technology to make the customer experience different. We sign customers in on iPads. Paperwork I signed electronically and updates are sent via text, email, logging on a website or as they wish. I want this innovation and image to come through in our cards

Target Market(s)

60%. Women 40% men. Age 35-60

Industry/Entity Type

Automotive

Requirements
Must have
• The card must have name, title, phone,email, cell, web page

```html
<!DOCTYPE html>
<html lang="en">
<head>
<meta charset="utf-8">
<title>Dentworks Garage — Business Card</title>
<link href="https://fonts.googleapis.com/css2?family=Source+Sans+3:wght@400;600;700&display=swap" rel="stylesheet">
<style>
  :root {
    --page-bg: #e4e5e7;
    --card-white: #f4f4f4;
    --card-white-edge: #e2e3e4;
    --green-light: #86c043;
    --green: #72b236;
    --green-dark: #5d9f2e;
    --green-pale: #c8dfae;
    --ink: #3a3a3a;
    --white: #ffffff;
  }
  * { box-sizing: border-box; margin: 0; padding: 0; }
  html, body { width: 883px; height: 1200px; overflow: hidden; }
  body {
    background: var(--page-bg);
    font-family: "Source Sans 3", sans-serif;
    position: relative;
  }
  .card {
    position: absolute;
    left: 91px;
    width: 700px;
    height: 400px;
    overflow: hidden;
    box-shadow: 0 6px 18px rgba(0,0,0,0.18);
  }
  .card--front { top: 150px; background: linear-gradient(160deg, var(--card-white), var(--card-white-edge)); }
  .card--back  { top: 650px; background: linear-gradient(135deg, var(--green-light) 0%, var(--green) 55%, var(--green-dark) 100%); }

  .front-panel { position: absolute; inset: 0; width: 100%; height: 100%; }

  .brand {
    position: absolute;
    font-weight: 700;
    letter-spacing: -0.5px;
    white-space: nowrap;
  }
  .card--front .brand {
    left: 40px; top: 172px;
    font-size: 40px;
    color: var(--green-dark);
  }
  .card--back .brand {
    left: 0; right: 0; top: 150px;
    text-align: center;
    font-size: 56px;
    color: var(--white);
  }
  .web-address {
    position: absolute;
    left: 0; right: 0; top: 262px;
    text-align: center;
    color: var(--white);
    font-size: 19px;
    font-weight: 600;
  }

  .contact {
    position: absolute;
    left: 445px; top: 48px;
    color: var(--white);
  }
  .contact__name { font-size: 26px; font-weight: 700; line-height: 1.1; }
  .contact__title { font-size: 17px; opacity: 0.85; margin-bottom: 26px; }
  .contact__list { list-style: none; }
  .contact__item {
    display: flex; align-items: center; gap: 10px;
    font-size: 19px; line-height: 32px;
  }
  .contact__item svg { width: 16px; height: 16px; flex: none; fill: var(--white); }
</style>
</head>
<body>

  <section class="card card--front" aria-label="Card front">
    <svg class="front-panel" viewBox="0 0 700 400" preserveAspectRatio="none" aria-hidden="true">
      <path d="M370 0 C 430 110, 430 290, 360 400 L 700 400 L 700 0 Z" fill="var(--green-pale)"/>
      <path d="M392 0 C 450 110, 450 290, 382 400 L 700 400 L 700 0 Z" fill="var(--green)"/>
    </svg>
    <div class="brand">dentworks garage</div>

    <div class="contact">
      <div class="contact__name">Ryan Mercer</div>
      <div class="contact__title">Managing Director</div>
      <ul class="contact__list">
        <li class="contact__item">
          <svg viewBox="0 0 16 16"><path d="M3 1l3 3-1.5 2a9 9 0 0 0 5.5 5.5L12 10l3 3-2 2C7 15 1 9 1 3z"/></svg>
          555.0142.3370
        </li>
        <li class="contact__item">
          <svg viewBox="0 0 16 16"><path d="M4 0h8a1 1 0 0 1 1 1v14a1 1 0 0 1-1 1H4a1 1 0 0 1-1-1V1a1 1 0 0 1 1-1zm1 2v10h6V2zm3 11a1 1 0 1 0 0 2 1 1 0 0 0 0-2z"/></svg>
          555.0142.3371
        </li>
        <li class="contact__item">
          <svg viewBox="0 0 16 16"><path d="M4 1h7v4H4zM1 6h14v7h-3v2H4v-2H1zm4 5v3h6v-3z"/></svg>
          555.0142.3372
        </li>
        <li class="contact__item">
          <svg viewBox="0 0 16 16"><path d="M1 3h14v1L8 9 1 4zm0 3l7 5 7-5v7H1z"/></svg>
          info@dentworksgarage.com
        </li>
        <li class="contact__item">
          <svg viewBox="0 0 16 16"><path d="M8 0a8 8 0 1 0 0 16A8 8 0 0 0 8 0zm0 1.5c1 1.2 1.6 3 1.8 5.5H6.2C6.4 4.5 7 2.7 8 1.5zM1.6 9h3c.1 2 .6 3.8 1.4 5A6.5 6.5 0 0 1 1.6 9zm4.6 0h3.6c-.2 2.4-.8 4.2-1.8 5.4-1-1.2-1.6-3-1.8-5.4zm5.2 0h3a6.5 6.5 0 0 1-4.4 5c.8-1.2 1.3-3 1.4-5zM1.6 7A6.5 6.5 0 0 1 6 2c-.8 1.2-1.3 3-1.4 5zm9.8 0c-.1-2-.6-3.8-1.4-5a6.5 6.5 0 0 1 4.4 5z"/></svg>
          www.dentworksgarage.com
        </li>
      </ul>
    </div>
  </section>

  <section class="card card--back" aria-label="Card back">
    <div class="brand">dentworks garage</div>
    <div class="web-address">www.dentworksgarage.com</div>
  </section>

</body>
</html>
```